Book Cover Design for first time business owners

Looking for a design for my book, 'FORGING A VENTURE' subtitle is
THE LEASING, LAYOUT, & BUILD-OUT METHODS FOR LAUNCHING YOUR SHOP OR EATERY IDEA WITHOUT DELAYS OR OVERSPENDING

If it helps, below is part of the preface:

These pages derive from my experiences and industry standards. This book runs through the budgeting, real estate, design, construction, signage, and equipment processes needed to get any retail or restaurant space open on-time and on budget while saving you time, money, and headaches along the way.

Whether it be a one-off enterprise or franchise, flower shop, or swim center; the steps and procedures are strikingly similar. Whether you’re looking to spend $200,000 or $2,000,000, it’s all largely the same.
This book does not discuss marketing or operations as those items are more concept specific, and outside the confines of this book.
Technically food-service concepts (restaurants, cafés, and bars) are not considered retail. For the basis of this book and to streamline writing, mentions of retail include food-service concepts.

Target Market(s)

First time business Owners looking to construct a retail or food-service concept

Font styles to use
Serif

Requirements
Must have
• I'm open to any designs! Looking for the design to wrap around the front, spine, and back.
• Please include the authors name on the front: Corwin Delaugh. The Authors name size should not be overly intrusive.
• I'm still working on the verbiage for the back of the book. That verbiage will be on the top half of the back.

```html
<!DOCTYPE html>
<html lang="en">
<head>
<meta charset="utf-8">
<title>Forging a Venture — Book Cover</title>
<link rel="stylesheet" href="https://fonts.googleapis.com/css2?family=Roboto+Serif:wdth,wght@50..150,400..600&display=swap">
<style>
  :root {
    --backdrop: #2f8a70;
    --paper: #ffffff;
    --ink: #1a1a1a;
    --ink-deep: #141414;
    --blue: #1f74bb;
    --red: #bb1b2c;
    --green: #8dc43f;
  }
  html, body {
    margin: 0;
    width: 1200px;
    height: 1200px;
    overflow: hidden;
    background: var(--backdrop);
  }
  .canvas {
    position: relative;
    width: 1200px;
    height: 1200px;
  }
  .book-cover {
    position: absolute;
    left: 225px;
    top: 38px;
    width: 750px;
    height: 1123px;
    display: block;
  }
  .cover-paper { fill: var(--paper); }
  .accent-bar { fill: var(--blue); }
  .dark-band { fill: var(--ink); }
  .dark-wedge { fill: var(--ink-deep); }
  .title {
    font-family: "Roboto Serif", Georgia, serif;
    font-stretch: 50%;
    font-weight: 400;
    font-size: 112px;
    fill: var(--paper);
    stroke: var(--ink);
    stroke-width: 3;
    paint-order: stroke;
  }
  .subtitle-ring {
    font-family: "Roboto Serif", Georgia, serif;
    font-stretch: 90%;
    font-weight: 600;
    font-size: 19px;
  }
  .subtitle-ring.on-dark { fill: var(--paper); }
  .subtitle-ring.on-light { fill: var(--ink); }
  .author-band { fill: var(--green); }
  .author {
    font-family: "Roboto Serif", Georgia, serif;
    font-stretch: 60%;
    font-weight: 600;
    font-size: 38px;
    fill: var(--ink);
  }
</style>
</head>
<body>
<main class="canvas">
  <svg class="book-cover" viewBox="370 157 738 1105" xmlns="http://www.w3.org/2000/svg" aria-label="Book cover: Forging a Venture by Corwin Delaugh">
    <defs>
      <clipPath id="cover-area">
        <rect x="370" y="157" width="738" height="1105"/>
      </clipPath>
      <clipPath id="dark-zones">
        <polygon points="370,340 890,654 370,1050"/>
        <polygon points="890,654 1108,487 1108,785"/>
      </clipPath>
      <clipPath id="light-zones">
        <polygon points="370,157 1108,157 1108,487 890,654 370,340"/>
        <polygon points="370,1050 890,654 1108,785 1108,1262 370,1262"/>
      </clipPath>
      <linearGradient id="emblem-tones" x1="0" y1="0" x2="0" y2="1">
        <stop offset="0" stop-color="#5a4a6e"/>
        <stop offset="0.55" stop-color="#3f6f8f"/>
        <stop offset="1" stop-color="#8dc43f"/>
      </linearGradient>
      <path id="ring-path" d="M 437 860 A 235 235 0 1 1 907 860 A 235 235 0 1 1 437 860"/>
    </defs>

    <g clip-path="url(#cover-area)">
      <rect class="cover-paper" x="370" y="157" width="738" height="1105"/>

      <g class="accent-bars">
        <polygon class="accent-bar" points="370,157 445,157 445,363 370,318"/>
        <polygon class="accent-bar" points="465,157 535,157 535,417 465,375"/>
        <polygon class="accent-bar" points="555,157 613,157 613,464 555,429"/>
      </g>

      <polygon class="dark-band" points="370,340 890,654 370,1050"/>
      <polygon class="dark-wedge" points="890,654 1108,487 1108,785"/>

      <text class="title" x="702" y="378" textLength="356" lengthAdjust="spacingAndGlyphs">FORGING</text>
      <text class="title" x="636" y="472" textLength="422" lengthAdjust="spacingAndGlyphs">A VENTURE</text>

      <circle class="emblem-area" role="img" aria-label="Circular storefront emblem with red, blue and green segments around a triangle" cx="672" cy="860" r="222" fill="url(#emblem-tones)"/>

      <g clip-path="url(#dark-zones)">
        <text class="subtitle-ring on-dark"><textPath href="#ring-path" textLength="1455" lengthAdjust="spacing">THE LEASING, LAYOUT, &amp; BUILD-OUT METHODS FOR LAUNCHING YOUR SHOP OR EATERY IDEA WITHOUT DELAYS OR OVERSPENDING.</textPath></text>
      </g>
      <g clip-path="url(#light-zones)">
        <text class="subtitle-ring on-light"><textPath href="#ring-path" textLength="1455" lengthAdjust="spacing">THE LEASING, LAYOUT, &amp; BUILD-OUT METHODS FOR LAUNCHING YOUR SHOP OR EATERY IDEA WITHOUT DELAYS OR OVERSPENDING.</textPath></text>
      </g>

      <polygon class="author-band" points="668,1262 820,1163 1108,1163 1108,1262"/>
      <text class="author" x="818" y="1224" textLength="219" lengthAdjust="spacingAndGlyphs">Corwin Delaugh</text>
    </g>
  </svg>
</main>
</body>
</html>
```